Robotic Physical Therapy office needs a Grand Opening Flyer

We need a Grand Opening flyer design for a robotic physical therapy office named Stellar Motion Therapy. We would like it to have a clean, classy, upscale feeling that gives potential clients a V.I.P. feeling. We would like to use the colors black, gray, and yellow (logo will be uploaded).

Event: Thursday, June 1st, 2023 from 12pm-6pm
location: 58274 Harlow Ave, Bloomfield Hills, MI 48319

Industry/Entity Type

Physical therapy

Font styles to use
Script

Colors

Designer to choose colors to be used in the design.

Requirements
Nice to have
• More of a vip feel for the invite

```html
<!DOCTYPE html>
<html lang="en">
<head>
<meta charset="utf-8">
<title>Stellar Motion Therapy – Grand Opening</title>
<link rel="stylesheet" href="https://fonts.googleapis.com/css2?family=Roboto:wght@400;700&display=swap">
<style>
  :root {
    --stage: #e4e4e4;
    --paper: #ffffff;
    --yellow: #f5d92e;
    --ink: #3a3645;
    --text: #1c1c1c;
    --photo-light: #d9dcdf;
    --photo-dark: #6f747b;
  }
  html, body {
    margin: 0;
    width: 1200px;
    height: 1200px;
    overflow: hidden;
    background: var(--stage);
  }
  .flyer-canvas {
    display: block;
    width: 1200px;
    height: 1200px;
  }
  .sheet { fill: var(--paper); }
  .accent { fill: var(--yellow); }
  .ink { fill: var(--ink); }
  .brand-name {
    font-family: "Roboto", sans-serif;
    font-weight: 700;
    font-size: 30px;
    fill: var(--ink);
  }
  .brand-dot { fill: var(--yellow); }
  .info-label {
    font-family: "Roboto", sans-serif;
    font-weight: 700;
    font-size: 22px;
    fill: var(--text);
  }
  .info-line {
    font-family: "Roboto", sans-serif;
    font-weight: 400;
    font-size: 19px;
    fill: var(--text);
  }
</style>
</head>
<body>
<svg class="flyer-canvas" viewBox="0 0 960 960" xmlns="http://www.w3.org/2000/svg">
  <defs>
    <linearGradient id="photo-tone" x1="0" y1="0" x2="1" y2="1">
      <stop offset="0" stop-color="var(--photo-light)"/>
      <stop offset="0.55" stop-color="#a9adb2"/>
      <stop offset="1" stop-color="var(--photo-dark)"/>
    </linearGradient>
    <clipPath id="sheet-clip">
      <rect x="180" y="52" width="600" height="853"/>
    </clipPath>
    <filter id="sheet-shadow" x="-5%" y="-5%" width="110%" height="110%">
      <feDropShadow dx="0" dy="2" stdDeviation="3" flood-opacity="0.25"/>
    </filter>
  </defs>

  <rect class="sheet" x="180" y="52" width="600" height="853" filter="url(#sheet-shadow)"/>

  <g class="flyer" clip-path="url(#sheet-clip)">
    <!-- brand -->
    <g class="brand">
      <circle class="brand-dot" cx="266" cy="151" r="26"/>
      <text class="brand-name" x="302" y="146">STELLAR MOTION</text>
      <text class="brand-name" x="302" y="184">THERAPY</text>
    </g>

    <!-- corner triangles -->
    <polygon class="ink" points="553,250 620,143 660,215"/>
    <polygon class="ink" points="775,128 790,110 790,150"/>

    <!-- honeycomb photo mosaic -->
    <g class="photo-mosaic" role="img" aria-label="Photo of a patient walking on a treadmill wearing a robotic leg exoskeleton in a therapy clinic" fill="url(#photo-tone)">
      <polygon points="200,375 231,318 293,318 324,375 293,432 231,432"/>
      <polygon points="200,493 231,436 293,436 324,493 293,550 231,550"/>
      <polygon points="308,316 339,259 401,259 432,316 401,373 339,373"/>
      <polygon points="308,433 339,376 401,376 432,433 401,490 339,490"/>
      <polygon points="308,551 339,494 401,494 432,551 401,608 339,608"/>
      <polygon points="416,375 447,318 509,318 540,375 509,432 447,432"/>
      <polygon points="416,493 447,436 509,436 540,493 509,550 447,550"/>
      <polygon points="524,316 555,259 617,259 648,316 617,373 555,373"/>
      <polygon points="524,433 555,376 617,376 648,433 617,490 555,490"/>
      <polygon points="524,551 555,494 617,494 648,551 617,608 555,608"/>
      <polygon points="632,252 663,195 725,195 756,252 725,309 663,309"/>
      <polygon points="632,375 663,318 725,318 756,375 725,432 663,432"/>
      <polygon points="632,493 663,436 725,436 756,493 725,550 663,550"/>
      <polygon points="740,316 771,259 833,259 864,316 833,373 771,373"/>
    </g>

    <!-- yellow accents -->
    <polygon class="accent" points="414,258 540,258 522,290 432,290"/>
    <polygon class="accent" points="448,555 510,555 540,608 420,608"/>
    <polygon class="accent" points="180,720 420,608 545,608 180,780"/>

    <!-- bottom frame -->
    <rect class="accent" x="180" y="770" width="33" height="135"/>
    <rect class="accent" x="180" y="877" width="418" height="28"/>
    <rect class="ink" x="598" y="877" width="182" height="28"/>

    <!-- event details -->
    <g class="event-details" text-anchor="middle">
      <text class="info-label" x="478" y="712">Event:</text>
      <text class="info-line" x="478" y="737">Thursday, June 1st, 2023</text>
      <text class="info-line" x="478" y="761">from 12pm-6pm</text>
      <text class="info-label" x="478" y="816">Location:</text>
      <text class="info-line" x="478" y="840">58274 Harlow Ave, Bloomfield Hills, MI 48319</text>
    </g>
  </g>
</svg>
</body>
</html>
```